Cutaneous Learning Clinical Treatments workbook New Word Template Design Project

Cutaneous Learning needs the old "Harbourview Derma Procedures Handbook" updated and given a fresh new look, using the new Cutaneous Learning logo.

The old workbook will be supplied to act as a guideline, but we'd like a fresh new look.

Target Market(s)

The people using this workbook are Dermal therapists and Dermal nurses.

Font styles to use
Serif
Sans Serif

Requirements
Must have
• The new logo incorporated on each page - obviously on the cover it will be a major focus, but on other pages we'd like to see the logo represented in a smaller way somehow.

Each module is to follow the same formula - as per the old workbook.

A4 portrait - 210mm X 297mm (8-1/4 X 11-3/4 inches)

The end result will be printed, so there must be space on the LH side to allow for binding
Nice to have
• We'd like the colour scheme of the new design to work in/match with the colour scheme of the logo.

Request from my boss - the final products we will need back are:
(1) an editable "in design" file
(2) pdf document

```html
<!DOCTYPE html>
<html lang="en">
<head>
<meta charset="utf-8">
<title>Cutaneous Learning — Clinical Treatments Workbook</title>
<link href="https://fonts.googleapis.com/css2?family=Oswald:wght@300;400&family=Roboto+Condensed:wght@400;500&display=swap" rel="stylesheet">
<style>
  :root{
    --navy:#121d4f;
    --navy-deep:#141a3a;
    --gold:#dbb640;
    --gold-label:#e3a126;
    --ink:#2a2a35;
    --rule:#a9b3c7;
    --cream:#faf1de;
    --backdrop:#e6e6e6;
    --paper:#ffffff;
  }
  *{box-sizing:border-box;margin:0;padding:0}
  html,body{width:1200px;height:1200px;overflow:hidden}
  body{background:var(--backdrop);position:relative;font-family:"Roboto Condensed",sans-serif;color:var(--ink)}
  .page{position:absolute;width:382px;height:495px;background:var(--paper);overflow:hidden}
  .page--cover{left:186px;top:78px;background:linear-gradient(#ffffff 35%,#e9e9ec 75%)}
  .page--toc-a{left:610px;top:78px}
  .page--toc-b{left:184px;top:618px}
  .page--intro{left:610px;top:618px}

  /* brand wordmark */
  .brand{font-family:"Oswald",sans-serif;font-weight:400;color:var(--navy);letter-spacing:.04em;white-space:nowrap;display:flex;align-items:center;gap:5px}
  .brand__mark{width:9px;height:9px;background:var(--navy)}
  .brand--cover{position:absolute;left:0;right:0;top:120px;justify-content:center;font-size:20px;flex-direction:column;gap:8px}
  .brand--cover .brand__mark{width:16px;height:16px;background:var(--gold)}
  .brand--header{position:absolute;right:24px;top:24px;font-size:12px}

  /* cover */
  .cover__title{position:absolute;left:0;right:0;top:200px;text-align:center;font-family:"Oswald",sans-serif;font-weight:300;font-size:33px;line-height:38px;color:var(--navy);transform:scaleY(1.08)}
  .cover__rule{position:absolute;left:75px;width:231px;top:285px;border-top:1px solid #555}
  .cover__staff{position:absolute;left:0;right:0;top:304px;text-align:center;font-size:8px;color:#444}
  .cover__line{position:absolute;left:93px;width:195px;top:344px;border-top:1px solid #555}
  .cover__band{position:absolute;left:0;right:0;top:392px;bottom:0;background:linear-gradient(180deg,var(--gold) 0,var(--gold) 14px,var(--navy) 14px,var(--navy) 100%)}

  /* page header */
  .page__title{position:absolute;left:22px;top:22px;font-family:"Oswald",sans-serif;font-weight:300;font-size:21px;color:var(--navy);letter-spacing:.01em}
  .page__rule{position:absolute;left:22px;right:20px;top:47px;border-top:1px solid var(--rule)}

  /* table of contents */
  .toc{position:absolute;left:24px;right:56px;list-style:none;font-size:6.4px;text-transform:uppercase}
  .toc li{display:grid;grid-template-columns:45px 1fr 20px;height:16.2px;align-items:center}
  .toc__num{color:var(--gold-label)}
  .toc__page{text-align:right}
  .toc--a{top:74px}
  .toc--b{top:76px;left:33px;right:40px}
  .toc--b li{height:16.4px;grid-template-columns:47px 1fr 20px}
  .toc__plain{grid-template-columns:1fr 20px !important}

  /* footer */
  .footer__line{position:absolute;left:0;width:258px;top:480px;border-top:1px solid var(--rule)}
  .footer__tab{position:absolute;left:263px;top:472px;width:70px;height:9px;background:var(--navy);color:#fff;font-size:6px;text-align:right;padding-right:6px;line-height:9px}
  .footer__accent{position:absolute;left:335px;top:472px;width:22px;height:9px;background:var(--gold-label)}

  /* introduction */
  .intro{position:absolute;left:34px;right:24px;top:84px;list-style:none;font-size:6.6px;line-height:10.4px}
  .intro li{display:grid;grid-template-columns:17px 1fr;margin-bottom:10px}
  .intro li:nth-child(3),.intro li:nth-child(4){margin-bottom:11px}
  .star{color:var(--navy);font-size:7px}
  .intro__note{color:#111}
  .finish{position:absolute;left:22px;top:344px;width:334px;height:102px;background:var(--cream);padding:10px 8px}
  .finish__title{text-align:center;font-family:"Oswald",sans-serif;font-weight:300;font-size:13px;color:var(--navy);margin-bottom:10px}
  .finish__cols{display:grid;grid-template-columns:1fr 1fr;font-size:6.4px;line-height:18px}
  .finish__col+.finish__col{border-left:1px solid #c9c2ae;padding-left:10px}
  .finish__col p{display:grid;grid-template-columns:11px 1fr}
</style>
</head>
<body>

<section class="page page--cover">
  <div class="cover__band" role="img" aria-label="Gold and navy decorative band across the foot of the cover"></div>
  <div class="brand brand--cover"><span class="brand__mark"></span><span>CUTANEOUS LEARNING</span></div>
  <h1 class="cover__title">CLINICAL<br>TREATMENTS WORKBOOK</h1>
  <div class="cover__rule"></div>
  <p class="cover__staff">STAFF NAME:</p>
  <div class="cover__line"></div>
</section>

<section class="page page--toc-a">
  <h2 class="page__title">TABLE OF CONTENTS</h2>
  <div class="brand brand--header"><span class="brand__mark"></span>CUTANEOUS LEARNING</div>
  <div class="page__rule"></div>
  <ul class="toc toc--a">
    <li class="toc__plain"><span>Introduction</span><span></span></li>
    <li class="toc__plain"><span>Workbook Summary</span><span class="toc__page">3</span></li>
    <li><span class="toc__num">Module 1:</span><span>Documentation for treatments</span><span class="toc__page">4</span></li>
    <li><span class="toc__num">Module 2:</span><span>Medical photography</span><span class="toc__page">5</span></li>
    <li><span class="toc__num">Module 3:</span><span>Infection prevention &amp; control</span><span class="toc__page">18</span></li>
    <li><span class="toc__num">Module 4:</span><span>Sterilisation</span><span class="toc__page">28</span></li>
    <li><span class="toc__num">Module 5:</span><span>Workspace maintenance</span><span class="toc__page">33</span></li>
    <li><span class="toc__num">Module 6:</span><span>Pathology collection</span><span class="toc__page">40</span></li>
    <li><span class="toc__num">Module 7:</span><span>Drugs &amp; poisons regulation</span><span class="toc__page">47</span></li>
    <li><span class="toc__num">Module 8:</span><span>Pre-op calls to patients</span><span class="toc__page">48</span></li>
    <li><span class="toc__num">Module 9:</span><span>Administering numbing cream</span><span class="toc__page">49</span></li>
    <li><span class="toc__num">Module 10:</span><span>Following up your patient post treatment</span><span class="toc__page">50</span></li>
    <li><span class="toc__num">Module 11:</span><span>Chemical peels</span><span class="toc__page">57</span></li>
    <li><span class="toc__num">Module 12:</span><span>Extractions (with Hyfrelux)</span><span class="toc__page">58</span></li>
    <li><span class="toc__num">Module 13:</span><span>L.E.D treatment</span><span class="toc__page">49</span></li>
    <li><span class="toc__num">Module 14:</span><span>Hair removal</span><span class="toc__page">49</span></li>
    <li><span class="toc__num">Module 15:</span><span>Broad band light treatment (BBL)</span><span class="toc__page">49</span></li>
    <li><span class="toc__num">Module 16:</span><span>Fractionated laser (Fraxia)</span><span class="toc__page">49</span></li>
    <li><span class="toc__num">Module 17:</span><span>Biophotonic treatment (Lumeris)</span><span class="toc__page">49</span></li>
    <li><span class="toc__num">Module 18:</span><span>Mela peels</span><span class="toc__page">49</span></li>
    <li><span class="toc__num">Module 19:</span><span>Pulsed dye laser (VascuPulse)</span><span class="toc__page">49</span></li>
    <li><span class="toc__num">Module 20:</span><span>Pico-second laser (pico for pigment)</span><span class="toc__page">49</span></li>
  </ul>
  <div class="footer__line"></div>
  <div class="footer__tab">Page 02</div>
  <div class="footer__accent"></div>
</section>

<section class="page page--toc-b">
  <h2 class="page__title">TABLE OF CONTENTS</h2>
  <div class="brand brand--header"><span class="brand__mark"></span>CUTANEOUS LEARNING</div>
  <div class="page__rule"></div>
  <ul class="toc toc--b">
    <li><span class="toc__num">Module 21:</span><span>Pico-second laser (pico tatoo removal)</span><span class="toc__page">49</span></li>
    <li><span class="toc__num">Module 22:</span><span>RF needling</span><span class="toc__page">49</span></li>
    <li><span class="toc__num">Module 23:</span><span>Vellora Pen</span><span class="toc__page">49</span></li>
    <li><span class="toc__num">Module 24:</span><span>Skin tightening (Thermalift)</span><span class="toc__page">49</span></li>
    <li><span class="toc__num">Module 25:</span><span>Skin tightening (RF tightening)</span><span class="toc__page">49</span></li>
    <li><span class="toc__num">Module 26:</span><span>CryoContour</span><span class="toc__page">49</span></li>
    <li><span class="toc__num">Module 27:</span><span>Skin tag removal</span><span class="toc__page">49</span></li>
    <li><span class="toc__num">Module 28:</span><span>AxillaDry</span><span class="toc__page">49</span></li>
    <li><span class="toc__num">Module 29:</span><span>PRP</span><span class="toc__page">49</span></li>
    <li><span class="toc__num">Module 30:</span><span>Injectables</span><span class="toc__page">49</span></li>
  </ul>
  <div class="footer__line"></div>
  <div class="footer__tab">Page 03</div>
  <div class="footer__accent"></div>
</section>

<section class="page page--intro">
  <h2 class="page__title">INTRODUCTION</h2>
  <div class="brand brand--header"><span class="brand__mark"></span>CUTANEOUS LEARNING</div>
  <div class="page__rule"></div>
  <ul class="intro">
    <li><span class="star">★</span><span>Welcome to our clinical team! We hope that you enjoy your time as a member of our dermatology team. To assist with your induction, please complete all sections of this workbook and bring it to your progress meetings with your manager.</span></li>
    <li><span class="star">★</span><span>Links to the theoretical components and exams can be found on our intranet, where we keep all of our reading material and videos.</span></li>
    <li><span class="star">★</span><span>All of your practical sheets in this workbook must be signed by an experienced member of our team.</span></li>
    <li><span class="star">★</span><span>Please also fill out the sign off sheet for each module to ensure that you have completed all components of the module and present to your manager for approval to begin treating patients.</span></li>
    <li><span class="star">★</span><span class="intro__note">Note: This Workbook Must Remain In A Secure Place At Work, As It Contains Patient Information And Must Not Be Taken Outside The Practice.</span></li>
    <li><span class="star">★</span><span>Progress meetings are highly recommended to make sure you are on the right track before you have completed too many sections and to make sure you are not needing to repeat any work!</span></li>
    <li><span class="star">★</span><span>You are expected to have completed modules 1 - 17 within 4 weeks of starting and modules 17 - 27 as arranged with your manager. Modules 28-30 are for nurses only, as arranged with your manager also. Please get busy finding opportunities to complete these sections - enjoy!</span></li>
  </ul>
  <div class="finish">
    <h3 class="finish__title">HOW TO FINISH THIS WORKBOOK</h3>
    <div class="finish__cols">
      <div class="finish__col">
        <p><span class="star">★</span><span>Read online theory and videos for each module</span></p>
        <p><span class="star">★</span><span>Complete online exam for each module</span></p>
        <p><span></span><span>Complete observations on your sign off sheet</span></p>
      </div>
      <div class="finish__col">
        <p><span class="star">★</span><span>Complete practical sheets in this workbook</span></p>
        <p><span class="star">★</span><span>Present completed sign off sheet to your manager</span></p>
        <p><span></span><span>for approval to begin each task</span></p>
      </div>
    </div>
  </div>
  <div class="footer__line"></div>
  <div class="footer__tab">Page 04</div>
  <div class="footer__accent"></div>
</section>

</body>
</html>
```